BrookPilot business cards

Software for fire departments

Target Market(s)

Fire Departments

Industry/Entity Type

Business

Contact Information for Business Card

see attachments. Looking to print three sets of cards.

Requirements
Must have
• front and back
Nice to have
• rounded corners

```html
<!DOCTYPE html>
<html lang="en">
<head>
<meta charset="utf-8">
<title>BrookPilot business card</title>
<link href="https://fonts.googleapis.com/css2?family=Caladea:ital,wght@0,400;0,700;1,400&display=swap" rel="stylesheet">
<style>
  :root {
    --brand-red: #e20e17;
    --ink-black: #0c0d0c;
    --paper: #ffffff;
    --card-w: 1200px;
    --card-h: 702px;
  }
  * { box-sizing: border-box; margin: 0; padding: 0; }
  html, body {
    width: var(--card-w);
    height: var(--card-h);
    overflow: hidden;
    background: var(--paper);
  }
  .card {
    position: relative;
    width: var(--card-w);
    height: var(--card-h);
    background: var(--paper);
    font-family: "Caladea", Georgia, serif;
    overflow: hidden;
  }
  .wave-header {
    position: absolute;
    inset: 0 0 auto 0;
    width: 100%;
    height: 220px;
  }
  .identity {
    position: absolute;
    top: 185px;
    left: 0;
    width: 100%;
    text-align: center;
    color: var(--brand-red);
  }
  .identity__name {
    font-weight: 700;
    font-size: 43px;
    line-height: 1.1;
  }
  .identity__title {
    font-style: italic;
    font-size: 41px;
    line-height: 1.25;
    margin-top: 4px;
  }
  .contact-strip__side {
    position: absolute;
    top: 351px;
    height: 167px;
    background: var(--ink-black);
  }
  .contact-strip__side--left { left: 0; width: 299px; }
  .contact-strip__side--right { left: 905px; width: 295px; }
  .contact-strip__details {
    position: absolute;
    top: 351px;
    left: 310px;
    width: 583px;
    height: 172px;
    background: var(--brand-red);
    color: var(--paper);
    font-size: 34px;
    line-height: 44px;
    text-align: center;
    padding-top: 21px;
  }
  .brand-name {
    position: absolute;
    top: 548px;
    left: 0;
    width: 100%;
    text-align: center;
    color: var(--brand-red);
    font-weight: 700;
    font-size: 36px;
  }
  .footer-band {
    position: absolute;
    left: 0;
    bottom: 0;
    width: 100%;
    height: 77px;
    background: var(--brand-red);
  }
  .footer-band__rule {
    position: absolute;
    top: 37px;
    height: 3px;
    background: var(--paper);
  }
  .footer-band__rule--left { left: 0; width: 372px; }
  .footer-band__rule--right { right: 0; width: 342px; }
  .footer-band__email {
    position: absolute;
    top: 0;
    left: 0;
    width: 100%;
    text-align: center;
    color: var(--paper);
    font-size: 39px;
    line-height: 77px;
  }
</style>
</head>
<body>
  <div class="card">
    <svg class="wave-header" viewBox="0 0 1200 220" preserveAspectRatio="none" aria-hidden="true">
      <path fill="var(--ink-black)" d="M0 0 H1200 V155 C1080 200 950 205 800 185 C600 158 360 60 170 82 C100 92 45 110 0 130 Z"/>
      <path fill="var(--brand-red)" d="M0 0 H1200 V140 C1080 185 950 190 800 170 C600 140 360 40 170 45 C100 48 45 55 0 60 Z"/>
    </svg>

    <div class="identity">
      <h1 class="identity__name">Mark Delaney</h1>
      <p class="identity__title">Chief Executive Officer</p>
    </div>

    <div class="contact-strip__side contact-strip__side--left"></div>
    <div class="contact-strip__details">
      <p>617-555-0142</p>
      <p>14 Harbor Mill Road</p>
      <p>Easton Falls, MA 01944</p>
    </div>
    <div class="contact-strip__side contact-strip__side--right"></div>

    <p class="brand-name">BrookPilot</p>

    <div class="footer-band">
      <span class="footer-band__rule footer-band__rule--left"></span>
      <span class="footer-band__rule footer-band__rule--right"></span>
      <p class="footer-band__email">mark@brookpilot.com</p>
    </div>
  </div>
</body>
</html>
```